Plakat für Verein
Zielgruppe
Wir möchten eine Veranstaltung für unseren Verein - Hinterkalmbacher Heimatpflegeverein machen.
Aufgabenstellung
Die Party der Golden 20er
Glanz-Glamour-Lebenslust
Tanzen wie früher - Feiern wie nie
21. März - Uhrzeit: 20.30 im Saal KM
Live mit DJaneMarlies
Dresscode: Goldene 20er - Fransen, Federn, Hosenträger, Zylinder
Farbe: Gold/Schgwarz

```html
<!DOCTYPE html>
<html lang="de">
<head>
<meta charset="utf-8">
<title>Die Party der Goldenen 20er – Plakat</title>
<link rel="stylesheet" href="https://fonts.googleapis.com/css2?family=Big+Shoulders+Display:wght@200&family=Mulish:wght@400;800&family=Questrial&display=swap">
<style>
  :root {
    --stage: #1b1517;
    --gold: #e9b83d;
    --gold-text: #ecbf45;
    --orange: #f08a45;
    --black: #000000;
    --white: #ffffff;
  }
  html, body {
    margin: 0;
    width: 1200px;
    height: 768px;
    overflow: hidden;
    background: var(--stage);
  }
  .canvas {
    position: relative;
    width: 1200px;
    height: 768px;
  }
  .poster-mount {
    position: absolute;
    left: 340px;
    top: 20px;
    width: 500px;
    height: 708px;
    padding: 10px;
    background: var(--gold);
  }
  .poster {
    position: relative;
    width: 500px;
    height: 708px;
    background: var(--black);
    overflow: hidden;
  }
  .deco-lines {
    position: absolute;
    inset: 0;
  }
  .corner-ornament {
    position: absolute;
    width: 86px;
    height: 86px;
    background: radial-gradient(circle at center, rgba(240,138,69,0.45), rgba(240,138,69,0.12) 70%);
  }
  .corner-ornament.top-left { left: 29px; top: 34px; }
  .corner-ornament.top-right { left: 386px; top: 34px; }
  .corner-ornament.bottom-left { left: 29px; top: 580px; }
  .corner-ornament.bottom-right { left: 386px; top: 580px; }
  .dancers {
    position: absolute;
    left: 178px;
    top: 78px;
    width: 144px;
    height: 124px;
    background: radial-gradient(ellipse at center, rgba(240,138,69,0.35), rgba(240,138,69,0.05) 75%);
  }
  .headline {
    position: absolute;
    left: 0;
    right: 0;
    top: 222px;
    margin: 0;
    text-align: center;
    font-family: "Big Shoulders Display", "Arial Narrow", sans-serif;
    font-weight: 200;
    font-size: 70px;
    line-height: 70px;
    color: var(--white);
    text-transform: uppercase;
  }
  .headline-line { display: block; }
  .headline-line.first { padding-left: 4px; }
  .subtitle {
    position: absolute;
    left: 0;
    right: 0;
    top: 398px;
    margin: 0;
    text-align: center;
    font-family: "Mulish", sans-serif;
    font-weight: 800;
    font-size: 23px;
    letter-spacing: 0.5px;
    color: var(--gold-text);
  }
  .tagline {
    position: absolute;
    left: 0;
    right: 0;
    top: 433px;
    margin: 0;
    text-align: center;
    font-family: "Questrial", sans-serif;
    font-size: 20px;
    color: var(--gold-text);
  }
  .event-details {
    position: absolute;
    left: 0;
    right: 0;
    top: 468px;
    margin: 0;
    text-align: center;
    font-family: "Mulish", sans-serif;
    font-weight: 800;
    font-size: 13px;
    line-height: 17px;
    color: var(--white);
  }
  .dresscode {
    position: absolute;
    left: 0;
    right: 0;
    top: 506px;
    margin: 0;
    text-align: center;
    font-family: "Questrial", sans-serif;
    font-size: 12px;
    line-height: 15px;
    color: var(--orange);
  }
  .country {
    position: absolute;
    top: 566px;
    margin: 0;
    font-family: "Questrial", sans-serif;
    font-size: 12px;
    color: var(--orange);
    transform: translateX(-50%);
  }
  .country.poland { left: 182px; }
  .country.sweden { left: 320px; }
  .club-seal {
    position: absolute;
    left: 192px;
    top: 574px;
    width: 112px;
    height: 112px;
    box-sizing: border-box;
    padding: 0 8px;
    border: 2px solid var(--orange);
    border-radius: 50%;
    background: var(--black);
    display: flex;
    align-items: center;
    justify-content: center;
    text-align: center;
  }
  .club-name {
    margin: 0;
    font-family: "Questrial", sans-serif;
    font-size: 8px;
    line-height: 12px;
    letter-spacing: 0.3px;
    color: var(--orange);
    text-transform: uppercase;
  }
</style>
</head>
<body>
<main class="canvas">
  <div class="poster-mount">
    <article class="poster">
      <svg class="deco-lines" width="500" height="708" viewBox="0 0 500 708" aria-hidden="true">
        <defs>
          <linearGradient id="rule-glow" x1="0" x2="1" y1="0" y2="0">
            <stop offset="0" stop-color="#f08a45"/>
            <stop offset="0.5" stop-color="#ffd2a8"/>
            <stop offset="1" stop-color="#f08a45"/>
          </linearGradient>
        </defs>
        <g fill="none" stroke="#f08a45" stroke-width="1.6">
          <rect x="29" y="34" width="443" height="632"/>
          <line x1="29" y1="230" x2="224" y2="35"/>
          <line x1="277" y1="35" x2="472" y2="230"/>
          <line x1="29" y1="470" x2="196" y2="666"/>
          <line x1="305" y1="666" x2="472" y2="470"/>
        </g>
        <line x1="97" y1="373" x2="402" y2="373" stroke="url(#rule-glow)" stroke-width="1.4"/>
      </svg>

      <div class="corner-ornament top-left" role="img" aria-label="Art-Deco-Ornament mit Strahlen und verschränkten Quadraten"></div>
      <div class="corner-ornament top-right" role="img" aria-label="Art-Deco-Ornament mit Strahlen und verschränkten Quadraten"></div>
      <div class="corner-ornament bottom-left" role="img" aria-label="Art-Deco-Ornament mit Strahlen und verschränkten Quadraten"></div>
      <div class="corner-ornament bottom-right" role="img" aria-label="Art-Deco-Ornament mit Strahlen und verschränkten Quadraten"></div>

      <div class="dancers" role="img" aria-label="Linienillustration eines tanzenden Charleston-Paares im Stil der 20er Jahre"></div>

      <h1 class="headline">
        <span class="headline-line first">Tanzen wie früher –</span>
        <span class="headline-line">Feiern wie nie</span>
      </h1>

      <h2 class="subtitle">DIE PARTY DER GOLDENEN 20ER</h2>
      <p class="tagline">Glanz &middot; Glamour &middot; Lebenslust</p>

      <p class="event-details">21. März / 20.30 Uhr / Saal KM<br>Live mit DJaneMarlies</p>

      <p class="dresscode">Dresscode: Goldene 20er.<br>Frauen: Fransen, Federn, Zylinder.<br>Männer: Anzug, Hosenträger, Hut</p>

      <p class="country poland">Polen</p>
      <p class="country sweden">Schweden</p>

      <div class="club-seal">
        <p class="club-name">Hinterkalmbacher<br>Heimatpflege-<br>verein</p>
      </div>
    </article>
  </div>
</main>
</body>
</html>
```